Web design concept for a IT recruitment agency.

Our website addresses two different target groups:
- Customers (companies) wanting to hire new IT talent
- It talent to find a new JOB

We a looking for a visual design concept that either addresses both target groups in one of the following options:
a. target both groups in 1 single splash page.
b. target both groups in 2 different pages one for both groups
c. or any creative third concept you can come up with

Requirements, we want one overall visual concept, that both target groups can relate to.

Trigger words what we want to express:
- passion / drive
- knowhow
- involvement
- professional/yet playful
- engagement

Background, company culture:
We are a recruitment agency with over 15 years of experience, we have no hard-sale culture.
But we emphasize on long term relationships, showing real interest in people and their needs.

Design requirements:
Use logo
Flat contemporary design

Target Market(s)

Industry/Entity Type

Hire

Number of Pages Required

2 page

Requirements
Must have
• We a looking for a visual design concept that either addresses both target groups

```html
<!DOCTYPE html>
<html lang="en">
<head>
<meta charset="utf-8">
<title>Brightwell Talent – IT Recruitment</title>
<link rel="stylesheet" href="https://fonts.googleapis.com/css2?family=Open+Sans:wght@400;600;700&display=swap">
<style>
:root{
  --blue:#1a8fdc;
  --blue-dark:#1576b8;
  --ink:#2d2d2d;
  --muted:#6b6b6b;
  --light:#f1f1f1;
  --footer:#2f2f2f;
  --footer-deep:#222;
  --white:#fff;
  --accent:#f08a1c;
  --star:#f5c518;
}
*{box-sizing:border-box;margin:0;padding:0}
html,body{width:1200px;height:2756px;overflow:hidden}
body{font-family:"Open Sans",Arial,sans-serif;color:var(--ink);background:var(--white)}
.container{width:960px;margin:0 auto;position:relative}

/* header */
.site-header{height:128px;background:var(--white);border-bottom:1px solid #e3e3e3}
.site-header .container{height:128px}
.brand{position:absolute;left:0;top:26px;display:flex;align-items:center;gap:14px}
.brand-mark{width:58px;height:58px;border-radius:50%;background:var(--blue)}
.brand-name{font-size:38px;font-weight:700;color:var(--ink);letter-spacing:-.5px}
.top-contact{position:absolute;right:0;top:18px;display:flex;align-items:center;gap:16px;font-size:20px;font-weight:600}
.top-contact svg{width:22px;height:22px}
.login-btn{background:var(--blue);color:var(--white);font-size:15px;padding:6px 18px;border-radius:3px;display:flex;gap:6px;align-items:center}
.main-nav{position:absolute;right:0;top:70px;display:flex;gap:0}
.main-nav a{font-size:15px;font-weight:600;color:var(--ink);text-decoration:none;padding:8px 15px;border-right:1px solid #ddd}
.main-nav a:last-child{border-right:0}
.main-nav a.active{background:var(--blue);color:var(--white)}

/* hero */
.hero{height:512px;position:relative;overflow:hidden}
.hero-visual{position:absolute;inset:0;background:linear-gradient(100deg,#8e9297 0%,#c6c9cc 30%,#eef0f2 55%,#f6f7f8 100%)}
.hero-copy{position:absolute;right:160px;top:150px;text-align:right}
.hero-copy h1{font-size:40px;line-height:1.25;font-weight:600;color:#333}
.hero-cta{display:inline-block;margin-top:28px;background:var(--blue);color:var(--white);font-size:22px;font-weight:700;padding:14px 26px;border-radius:3px}
.slider-arrow{position:absolute;top:232px;width:34px;height:48px;background:#333;display:flex;align-items:center;justify-content:center}
.slider-arrow.prev{left:0}.slider-arrow.next{right:0}

/* welcome */
.welcome{height:380px;padding-top:38px}
.section-title{font-size:40px;font-weight:400;color:#333;text-align:center}
.section-title strong{color:var(--blue);font-weight:600}
.title-rule{width:960px;height:2px;background:#ddd;margin:16px auto 0;position:relative}
.title-rule:after{content:"";position:absolute;left:0;top:0;width:180px;height:2px;background:var(--blue)}
.welcome-body{display:flex;gap:30px;margin-top:28px}
.team-photo{width:272px;height:220px;flex:none;background:linear-gradient(180deg,#e9ecef,#b9c0c8 60%,#4c5966)}
.welcome-body p{font-size:15px;line-height:1.65;color:var(--muted)}
.welcome-body a{color:var(--blue)}

/* services */
.services{height:520px;background:var(--blue);color:var(--white);padding-top:60px;text-align:center}
.services h2{font-size:40px;font-weight:400;display:flex;justify-content:center;align-items:center;gap:14px}
.services .title-rule{width:960px;background:rgba(255,255,255,.35)}
.services .title-rule:after{background:var(--white);left:390px}
.service-list{display:flex;justify-content:center;gap:120px;margin-top:42px}
.service{width:340px}
.service-icon{width:116px;height:116px;border-radius:50%;background:var(--white);margin:0 auto;display:flex;align-items:center;justify-content:center}
.service h3{font-size:28px;font-weight:600;margin-top:18px}
.service p{font-size:14px;line-height:1.55;margin-top:10px;opacity:.92}
.btn-outline{display:inline-block;margin-top:18px;font-size:13px;font-weight:700;padding:8px 16px;background:var(--blue-dark);border:1px solid rgba(255,255,255,.6)}

/* stories */
.stories{height:460px;position:relative;overflow:hidden;text-align:center;color:var(--white)}
.stories-visual{position:absolute;inset:0;background:linear-gradient(180deg,#7d7f82 0%,#5a5c5f 45%,#3b3c3e 100%)}
.stories .container{padding-top:38px}
.stories h2{font-size:40px;font-weight:600}
.stories .title-rule{background:rgba(255,255,255,.3)}
.stories .title-rule:after{left:390px;background:var(--white)}
.client-avatar{width:92px;height:92px;border-radius:50%;border:4px solid var(--white);margin:24px auto 0;background:linear-gradient(180deg,#c9ccd0,#7d8690)}
.client-name{font-size:14px;margin-top:8px}
.stars{margin-top:6px;display:flex;justify-content:center;gap:4px}
.quote{font-size:15px;line-height:1.6;margin:18px auto 0;width:920px;font-style:italic;color:#e6e6e6}
.quote b{font-size:34px;vertical-align:-8px;font-style:normal}

/* why */
.why{height:420px;background:var(--light);position:relative;overflow:hidden}
.why .container{padding-top:28px}
.why-copy{width:520px}
.why h2{font-size:40px;font-weight:600;color:#444}
.why .lead{font-size:19px;font-weight:700;color:#555;line-height:1.35;margin-top:10px}
.why ul{list-style:none;margin-top:18px}
.why li{font-size:14px;line-height:1.6;color:var(--muted);padding-left:24px;position:relative;margin-bottom:14px}
.why li:before{content:"";position:absolute;left:4px;top:7px;width:9px;height:9px;border-radius:50%;border:2px solid var(--blue)}
.why-photo{position:absolute;left:640px;top:12px;width:620px;height:440px;border-radius:50%;border:10px solid var(--white);background:linear-gradient(150deg,#f4f5f6,#c8cdd3 50%,#5b6470)}

/* footer */
.site-footer{height:300px;background:var(--footer);color:#cfcfcf}
.footer-cols{display:flex;padding-top:26px}
.footer-col{width:240px}
.footer-col h4{font-size:17px;color:var(--white);font-weight:600;margin-bottom:14px}
.footer-col ul{list-style:none}
.footer-col li{font-size:13px;padding:7px 0;border-bottom:1px solid #444;width:180px}
.field{width:210px;height:30px;background:#3d3d3d;border:1px solid #4a4a4a;margin-bottom:8px;font-size:12px;color:#999;padding:6px 10px}
.field.tall{height:60px}
.submit{background:var(--accent);color:var(--white);font-size:12px;font-weight:700;padding:6px 16px;display:inline-block}
.contact-line{font-size:13px;line-height:1.6;display:flex;gap:8px;align-items:flex-start;margin-bottom:8px}
.contact-line svg{flex:none;margin-top:3px}
.social{display:flex;align-items:center;gap:12px;font-size:13px;margin-bottom:14px}
.social span.sq{width:30px;height:30px;background:#4b4b4b;display:block}
.copyright{height:36px;background:var(--footer-deep);color:#aaa;font-size:12px;text-align:center;line-height:36px}
</style>
</head>
<body>

<header class="site-header">
  <div class="container">
    <div class="brand"><span class="brand-mark"></span><span class="brand-name">Brightwell Talent</span></div>
    <div class="top-contact">
      <span style="display:flex;gap:8px;align-items:center">
        <svg viewBox="0 0 24 24"><path fill="#1a8fdc" d="M6.6 10.8a15 15 0 0 0 6.6 6.6l2.2-2.2a1 1 0 0 1 1-.25 11.4 11.4 0 0 0 3.6.57 1 1 0 0 1 1 1V20a1 1 0 0 1-1 1A17 17 0 0 1 3 4a1 1 0 0 1 1-1h3.5a1 1 0 0 1 1 1c0 1.25.2 2.45.57 3.57a1 1 0 0 1-.25 1z"/></svg>
        012-555-0147
      </span>
      <span class="login-btn">
        <svg viewBox="0 0 24 24" style="width:14px;height:14px"><rect x="5" y="10" width="14" height="11" fill="#fff"/><path d="M8 10V7a4 4 0 0 1 8 0v3" stroke="#fff" stroke-width="2" fill="none"/></svg>
        Login
      </span>
    </div>
    <nav class="main-nav">
      <a class="active">HOME</a><a>ABOUT US</a><a>OUR SERVICES</a><a>WHY CHOOSE US</a><a>CONTACT US</a>
    </nav>
  </div>
</header>

<section class="hero">
  <div class="hero-visual" role="img" aria-label="Photo of a businessman in a suit holding a magnifying glass over a candidate profile icon"></div>
  <div class="hero-copy">
    <h1>Staffing Solutions<br>For You &amp; New Approach<br>To Recruiting</h1>
    <span class="hero-cta">GET STARTED WITH US</span>
  </div>
  <span class="slider-arrow prev"><svg width="12" height="18" viewBox="0 0 12 18"><path d="M10 2 3 9l7 7" stroke="#fff" stroke-width="2.5" fill="none"/></svg></span>
  <span class="slider-arrow next"><svg width="12" height="18" viewBox="0 0 12 18"><path d="m2 2 7 7-7 7" stroke="#fff" stroke-width="2.5" fill="none"/></svg></span>
</section>

<section class="welcome">
  <div class="container">
    <h2 class="section-title">Welcome to <strong>Brightwell Talent</strong></h2>
    <div class="title-rule"></div>
    <div class="welcome-body">
      <div class="team-photo" role="img" aria-label="Photo of a smiling business team in suits standing together"></div>
      <p>We match growing companies with skilled IT professionals who care about their craft. For over fifteen years our team has built lasting relationships by listening first, understanding real needs and taking the time to find the right fit. We do not push quick placements. Instead we stay involved before, during and after every hire, so both the company and the candidate feel supported. Our consultants know the technology landscape, speak the language of developers and managers alike, and bring genuine passion to every conversation. Whether you are hiring or searching, we are ready to help you take the next step with confidence. <a>[+]</a></p>
    </div>
  </div>
</section>

<section class="services">
  <div class="container">
    <h2>
      <svg width="40" height="40" viewBox="0 0 24 24"><path fill="#fff" d="M19.4 13a7.5 7.5 0 0 0 0-2l2.1-1.6-2-3.4-2.5 1a7 7 0 0 0-1.7-1L15 3h-4l-.4 2.9a7 7 0 0 0-1.7 1l-2.5-1-2 3.4L6.6 11a7.5 7.5 0 0 0 0 2l-2.1 1.6 2 3.4 2.5-1a7 7 0 0 0 1.7 1L11 21h4l.4-2.9a7 7 0 0 0 1.7-1l2.5 1 2-3.4zM13 15.5A3.5 3.5 0 1 1 13 8.5a3.5 3.5 0 0 1 0 7z"/></svg>
      Our Services
    </h2>
    <div class="title-rule"></div>
    <div class="service-list">
      <div class="service">
        <div class="service-icon">
          <svg width="64" height="64" viewBox="0 0 64 64"><circle cx="32" cy="20" r="9" fill="#1a8fdc"/><path d="M16 48a16 16 0 0 1 32 0z" fill="#1a8fdc"/><circle cx="12" cy="26" r="6" fill="#1576b8"/><path d="M2 48a10 10 0 0 1 20 0z" fill="#1576b8"/><circle cx="52" cy="26" r="6" fill="#1576b8"/><path d="M42 48a10 10 0 0 1 20 0z" fill="#1576b8"/></svg>
        </div>
        <h3>Recruiting</h3>
        <p>Tell us about your team and the skills you need. We search, screen and introduce IT talent that fits your culture and goals.</p>
        <span class="btn-outline">READ MORE</span>
      </div>
      <div class="service">
        <div class="service-icon">
          <svg width="64" height="64" viewBox="0 0 64 64"><circle cx="20" cy="20" r="8" fill="#1a8fdc"/><path d="M6 46a14 14 0 0 1 28 0z" fill="#1a8fdc"/><circle cx="44" cy="20" r="8" fill="#1576b8"/><path d="M30 46a14 14 0 0 1 28 0z" fill="#1576b8"/><rect x="22" y="50" width="20" height="6" rx="3" fill="#1a8fdc"/></svg>
        </div>
        <h3>Employment</h3>
        <p>Looking for your next IT role? We listen to what drives you and connect you with employers who value your knowhow.</p>
        <span class="btn-outline">READ MORE</span>
      </div>
    </div>
  </div>
</section>

<section class="stories">
  <div class="stories-visual" role="img" aria-label="Blurred photo of a cheering office team celebrating success"></div>
  <div class="container">
    <h2>Success Stories</h2>
    <div class="title-rule"></div>
    <div class="client-avatar" role="img" aria-label="Portrait photo of the client"></div>
    <p class="client-name">Mr. Daniel Marsh</p>
    <div class="stars">
      <svg width="90" height="16" viewBox="0 0 90 16"><g fill="#f5c518"><polygon points="8,0 10,6 16,6 11,10 13,16 8,12 3,16 5,10 0,6 6,6"/><polygon transform="translate(18)" points="8,0 10,6 16,6 11,10 13,16 8,12 3,16 5,10 0,6 6,6"/><polygon transform="translate(36)" points="8,0 10,6 16,6 11,10 13,16 8,12 3,16 5,10 0,6 6,6"/><polygon transform="translate(54)" points="8,0 10,6 16,6 11,10 13,16 8,12 3,16 5,10 0,6 6,6"/><polygon transform="translate(72)" points="8,0 10,6 16,6 11,10 13,16 8,12 3,16 5,10 0,6 6,6"/></g></svg>
    </div>
    <p class="quote"><b>“</b> They took the time to understand what our development team really needed. Within weeks we met three strong candidates, and the engineer we hired is still with us today. The whole process felt personal, honest and refreshingly relaxed from start to finish. <b>”</b></p>
  </div>
</section>

<section class="why">
  <div class="why-photo" role="img" aria-label="Photo of business colleagues reviewing documents together at a desk"></div>
  <div class="container">
    <div class="why-copy">
      <h2>Why Choose Us</h2>
      <p class="lead">We love finding great people great jobs. This is what we do and we believe we are really good at it.</p>
      <ul>
        <li>We take time to understand the culture of every client and the ambitions of every candidate, so each introduction makes sense for both sides.</li>
        <li>Our consultants have worked in IT themselves, which means we speak your language and can judge technical skills with real knowhow.</li>
      </ul>
    </div>
  </div>
</section>

<footer class="site-footer">
  <div class="container footer-cols">
    <div class="footer-col">
      <h4>Quick Links</h4>
      <ul><li>Home</li><li>About Us</li><li>Our Services</li><li>Why Choose Us</li><li>Contact Us</li></ul>
    </div>
    <div class="footer-col">
      <h4>Quick Contact</h4>
      <div class="field">Name</div>
      <div class="field">Email</div>
      <div class="field tall">Message</div>
      <span class="submit">SUBMIT</span>
    </div>
    <div class="footer-col">
      <h4>Contact Detail</h4>
      <div class="contact-line">
        <svg width="12" height="16" viewBox="0 0 12 16"><path d="M6 0a6 6 0 0 0-6 6c0 4.5 6 10 6 10s6-5.5 6-10a6 6 0 0 0-6-6zm0 8.5A2.5 2.5 0 1 1 6 3.5a2.5 2.5 0 0 1 0 5z" fill="#1a8fdc"/></svg>
        <span>Brightwell Talent<br>24 Orchard Row, Suite 5<br>Northfield, ZN 40210</span>
      </div>
      <div class="contact-line">
        <svg width="12" height="12" viewBox="0 0 24 24"><path fill="#1a8fdc" d="M6.6 10.8a15 15 0 0 0 6.6 6.6l2.2-2.2a1 1 0 0 1 1-.25 11.4 11.4 0 0 0 3.6.57 1 1 0 0 1 1 1V20a1 1 0 0 1-1 1A17 17 0 0 1 3 4a1 1 0 0 1 1-1h3.5a1 1 0 0 1 1 1c0 1.25.2 2.45.57 3.57a1 1 0 0 1-.25 1z"/></svg>
        <span>012-555-0147</span>
      </div>
      <div class="contact-line">
        <svg width="12" height="12" viewBox="0 0 24 24"><path fill="#1a8fdc" d="M6.6 10.8a15 15 0 0 0 6.6 6.6l2.2-2.2a1 1 0 0 1 1-.25 11.4 11.4 0 0 0 3.6.57 1 1 0 0 1 1 1V20a1 1 0 0 1-1 1A17 17 0 0 1 3 4a1 1 0 0 1 1-1h3.5a1 1 0 0 1 1 1c0 1.25.2 2.45.57 3.57a1 1 0 0 1-.25 1z"/></svg>
        <span>012-555-0148</span>
      </div>
      <div class="contact-line">
        <svg width="14" height="12" viewBox="0 0 14 12"><rect x=".5" y=".5" width="13" height="11" fill="none" stroke="#1a8fdc"/><path d="M.5.5 7 6l6.5-5.5" fill="none" stroke="#1a8fdc"/></svg>
        <span>hello@brightwelltalent.com</span>
      </div>
    </div>
    <div class="footer-col">
      <h4>Follow Us</h4>
      <div class="social"><span class="sq"></span>Friendsboard</div>
      <div class="social"><span class="sq"></span>Chirpline</div>
      <div class="social"><span class="sq"></span>Globeplus</div>
      <div class="social"><span class="sq"></span>Workconnect</div>
    </div>
  </div>
</footer>
<div class="copyright">© Copyright 2015 Brightwell Talent | All Rights Reserved</div>

</body>
</html>
```